Graphic to communicate emotional connection

Howdy-I need a graphic that describe my financial planning process.The attached is a concept, but please use your own creativity to show how you would display this:- The four circles on the outside (Protect what we have, know where it goes, make it grow, and dignity and independence) are the four major areas of concern- Then, there are three value statements:- The first is the most powerful which is that Clarity leads to Control which allows your Intentions to come through- The second shows that we take our clients from Uncertainty and Confusion, to Confidence and Intention- The third says we create space for you to develop your Purposeful Effort which leads to Your Best Financial Life.I've also attached my logo - please use the colors in my logo and maybe add a soft green as needed.The reader should be able to briefly scan this document and understand that we will connect with them on an emotional level to get their finances in shape.Thanks!-Tam

Target Market(s)

wealthy women, whether independent or married

Industry/Entity Type

Financial Planning

Requirements
Must have
• Please use the colors in my logo plus a soft green as needed
Should not have
• This should not be a busy or hard-to-read graphic. It is meant to convey an that I try to make an emotional connection, at a glance.

```html
<!DOCTYPE html>
<html lang="en">
<head>
<meta charset="utf-8">
<title>Financial Planning Process</title>
<link rel="stylesheet" href="https://fonts.googleapis.com/css2?family=Mulish:wght@400;500;600&display=swap">
<style>
  :root {
    --green: #74b97a;
    --green-soft: #c6eeae;
    --navy: #214a8b;
    --ink: #666666;
    --ring: #666666;
    --paper: #f8f8f8;
    --bg-edge: #e3e3e3;
    --bg-center: #ffffff;
    --placeholder: #dedede;
  }
  html, body {
    margin: 0;
    padding: 0;
    width: 1200px;
    height: 911px;
    overflow: hidden;
  }
  body {
    background: radial-gradient(ellipse at 50% 50%, var(--bg-center) 0%, #f4f4f4 45%, var(--bg-edge) 100%);
    font-family: "Mulish", Arial, sans-serif;
  }
  .process-map { display: block; width: 1200px; height: 911px; }
  .frame-line { stroke: var(--green); stroke-width: 4.5; fill: none; }
  .concern-outer { fill: var(--green); }
  .concern-ring { fill: var(--paper); stroke: var(--ring); stroke-width: 9; }
  .concern-rule { stroke: var(--ring); stroke-width: 2; }
  .concern-text { fill: var(--ink); font-size: 19px; font-weight: 400; text-anchor: middle; letter-spacing: 0.2px; }
  .concern-text.small { font-size: 15.5px; }
  .link-line { stroke: var(--green); stroke-width: 2; }
  .step-base { fill: var(--green-soft); stroke: var(--green); stroke-width: 1.5; }
  .step-arc { fill: none; stroke: var(--green); stroke-width: 6; }
  .step-ring { fill: var(--paper); stroke: var(--navy); stroke-width: 9; }
  .next-dot { fill: var(--navy); }
  .next-chevron { fill: none; stroke: #ffffff; stroke-width: 3; stroke-linecap: round; stroke-linejoin: round; }
  .step-label { fill: var(--ink); font-size: 21px; font-weight: 600; text-anchor: middle; letter-spacing: 0.6px; }
  .step-label.small { font-size: 14px; letter-spacing: 0.4px; }
  .leads-to { fill: #555555; font-size: 9.5px; font-weight: 500; text-anchor: middle; }
  .arc-caption { fill: var(--ink); font-size: 12px; font-weight: 500; letter-spacing: 0.5px; }
  .icon-stroke { fill: none; stroke: var(--ink); }
  .icon-fill { fill: var(--ink); }
  .figure-slot { fill: var(--placeholder); }
</style>
</head>
<body>
<svg class="process-map" viewBox="0 0 1200 911" xmlns="http://www.w3.org/2000/svg">
  <defs>
    <path id="arc-take" d="M421.1,489.2 A70,70 0 0 1 555.8,453.1"/>
    <path id="arc-create" d="M431,710.3 A72,72 0 1 1 561.7,662.7"/>
  </defs>

  <g class="frame">
    <line class="frame-line" x1="246" y1="141" x2="953" y2="141"/>
    <line class="frame-line" x1="246" y1="779" x2="953" y2="779"/>
    <line class="frame-line" x1="246" y1="141" x2="246" y2="763"/>
    <line class="frame-line" x1="953" y1="141" x2="953" y2="763"/>
  </g>

  <g class="concern" transform="translate(246,141)">
    <circle class="concern-outer" r="87"/>
    <circle class="concern-ring" r="69"/>
    <line class="concern-rule" x1="-23" y1="-42" x2="23" y2="-42"/>
    <text class="concern-text" y="-19">PROTECT</text>
    <text class="concern-text" y="3">WHAT</text>
    <text class="concern-text" y="25">WE HAVE</text>
    <line class="concern-rule" x1="-23" y1="36" x2="23" y2="36"/>
  </g>
  <g class="concern" transform="translate(953,141)">
    <circle class="concern-outer" r="87"/>
    <circle class="concern-ring" r="69"/>
    <line class="concern-rule" x1="-23" y1="-42" x2="23" y2="-42"/>
    <text class="concern-text" y="-17">KNOW</text>
    <text class="concern-text" y="4">WHERE</text>
    <text class="concern-text" y="26">IT GOES</text>
    <line class="concern-rule" x1="-23" y1="36" x2="23" y2="36"/>
  </g>
  <g class="concern" transform="translate(246,763)">
    <circle class="concern-outer" r="87"/>
    <circle class="concern-ring" r="69"/>
    <line class="concern-rule" x1="-23" y1="-35" x2="23" y2="-35"/>
    <text class="concern-text" y="-6">MAKE</text>
    <text class="concern-text" y="16">IT GROW</text>
    <line class="concern-rule" x1="-23" y1="30" x2="23" y2="30"/>
  </g>
  <g class="concern" transform="translate(953,763)">
    <circle class="concern-outer" r="87"/>
    <circle class="concern-ring" r="69"/>
    <line class="concern-rule" x1="-23" y1="-34" x2="23" y2="-34"/>
    <text class="concern-text small" y="-13">DIGNITY</text>
    <text class="concern-text small" y="4">AND</text>
    <text class="concern-text small" y="20">INDEPENDENCE</text>
    <line class="concern-rule" x1="-23" y1="30" x2="23" y2="30"/>
  </g>

  <g class="statement statement-core">
    <line class="link-line" x1="381" y1="279" x2="819" y2="279"/>

    <g class="step" transform="translate(381,279)">
      <circle class="step-base" r="60"/>
      <circle class="step-arc" r="62" stroke-dasharray="97 300" transform="rotate(180)"/>
      <circle class="step-ring" r="46"/>
      <g class="icon icon-search">
        <circle class="icon-stroke" cx="-4" cy="-5" r="13" stroke-width="5"/>
        <line class="icon-stroke" x1="6" y1="5" x2="17" y2="16" stroke-width="6" stroke-linecap="round"/>
      </g>
    </g>

    <g class="step" transform="translate(600,279)">
      <circle class="step-base" r="60"/>
      <circle class="step-arc" r="62" stroke-dasharray="65 330" transform="rotate(240)"/>
      <circle class="step-ring" r="46"/>
      <g class="icon icon-gears">
        <circle class="icon-stroke" cx="-9" cy="-9" r="11" stroke-width="7" stroke-dasharray="4.3 4.3"/>
        <circle class="icon-stroke" cx="-9" cy="-9" r="7" stroke-width="5"/>
        <circle class="icon-stroke" cx="13" cy="13" r="8" stroke-width="6" stroke-dasharray="3.5 3.5"/>
        <circle class="icon-stroke" cx="13" cy="13" r="5" stroke-width="4"/>
      </g>
    </g>

    <g class="step" transform="translate(819,279)">
      <circle class="step-base" r="60"/>
      <circle class="step-arc" r="62" stroke-dasharray="97 300" transform="rotate(270)"/>
      <circle class="step-ring" r="46"/>
      <g class="icon icon-target">
        <circle class="icon-stroke" r="24" stroke-width="4"/>
        <circle class="icon-stroke" r="16" stroke-width="4"/>
        <circle class="icon-stroke" r="8" stroke-width="4"/>
        <circle class="icon-fill" r="3"/>
        <line class="icon-stroke" x1="0" y1="0" x2="22" y2="-22" stroke-width="3"/>
        <path class="icon-fill" d="M18,-26 L28,-28 L26,-18 Z"/>
      </g>
    </g>

    <g class="next" transform="translate(490,279)">
      <circle class="next-dot" r="14"/>
      <path class="next-chevron" d="M-3,-6 L3,0 L-3,6"/>
    </g>
    <g class="next" transform="translate(710,279)">
      <circle class="next-dot" r="14"/>
      <path class="next-chevron" d="M-3,-6 L3,0 L-3,6"/>
    </g>

    <text class="step-label" x="381" y="369">CLARITY</text>
    <text class="step-label" x="600" y="369">CONTROL</text>
    <text class="step-label" x="818" y="369">INTENTION</text>
  </g>

  <g class="statement statement-journey">
    <line class="link-line" x1="490" y1="477" x2="718" y2="477"/>
    <text class="arc-caption"><textPath href="#arc-take">WE TAKE YOU FROM</textPath></text>

    <g class="step" transform="translate(490,477)">
      <circle class="step-base" r="55"/>
      <circle class="step-arc" r="57" stroke-dasharray="90 300" transform="rotate(180)"/>
      <circle class="step-ring" r="42"/>
      <circle class="figure-slot" r="32" role="img" aria-label="Icon of a person scratching their head, unsure which way to go"/>
    </g>
    <g class="step" transform="translate(718,477)">
      <circle class="step-base" r="55"/>
      <circle class="step-arc" r="57" stroke-dasharray="90 300" transform="rotate(270)"/>
      <circle class="step-ring" r="42"/>
      <circle class="figure-slot" r="32" role="img" aria-label="Icon of a person standing confidently with folded arms"/>
    </g>

    <text class="leads-to" x="603" y="458">WHICH LEADS TO</text>
    <g class="next" transform="translate(604,477)">
      <circle class="next-dot" r="14"/>
      <path class="next-chevron" d="M-3,-6 L3,0 L-3,6"/>
    </g>

    <text class="step-label small" x="490" y="549">UNCERTANITY CONFUSION</text>
    <text class="step-label small" x="719" y="549">CONFIDENCE INTENTION</text>
  </g>

  <g class="statement statement-growth">
    <line class="link-line" x1="490" y1="669" x2="718" y2="669"/>
    <text class="arc-caption"><textPath href="#arc-create">WE CREATE SPACE FOR YOUR</textPath></text>

    <g class="step" transform="translate(490,669)">
      <circle class="step-base" r="55"/>
      <circle class="step-arc" r="57" stroke-dasharray="90 300" transform="rotate(180)"/>
      <circle class="step-ring" r="42"/>
      <circle class="figure-slot" r="32" role="img" aria-label="Icon of a person pushing a large gear"/>
    </g>
    <g class="step" transform="translate(718,669)">
      <circle class="step-base" r="55"/>
      <circle class="step-arc" r="57" stroke-dasharray="90 300" transform="rotate(270)"/>
      <circle class="step-ring" r="42"/>
      <circle class="figure-slot" r="32" role="img" aria-label="Icon of a potted plant growing a dollar-sign leaf"/>
    </g>

    <text class="leads-to" x="603" y="652">WHICH LEADS TO</text>
    <g class="next" transform="translate(604,669)">
      <circle class="next-dot" r="14"/>
      <path class="next-chevron" d="M-3,-6 L3,0 L-3,6"/>
    </g>

    <text class="step-label small" x="490" y="744">PURPOSEFUL EFFORT</text>
    <text class="step-label small" x="719" y="744">YOUR BEST FINANCIAL LIFE</text>
  </g>
</svg>
</body>
</html>
```